Mental Health Services for Employees - we need a website for our new business

We need a simple web design to showcase our various services. Our programs help organizations to ensure the heath and wellness of their workers. Our company is called "Brightway Workplace Partners Inc." or "Brightway" We'd like to see designs that use the colour palette from our logo. Our customers our fairly conservative, and our design should communicate due diligence around providing a safe and healthy environment for workers. Attached our the logo files. Also sample photographs from our purchased images - others available. Original design for website is found here: https://lanternow7.examplesite.com/mypage-1 A key page not listed in our original design is a section that lists "Five Reasons to Work With Us". We will need to be able to modify and change the copy/menu options as the business grows.

Target Market(s)

businesses who want to provide health and wellness services for their employees

Coding

Coded - Design and coding required

Number of Pages Required

2 page

Font styles to use
Sans Serif

Requirements
Must have
• colours that work with our attached logo

```html
<!DOCTYPE html>
<html lang="en">
<head>
<meta charset="utf-8">
<title>Brightway Workplace Partners</title>
<link href="https://fonts.googleapis.com/css2?family=Barlow:ital,wght@0,400;0,500;0,600;0,700;0,800;1,400;1,600;1,700&display=swap" rel="stylesheet">
<style>
:root{
  --teal:#15a597;
  --green:#1f9a6d;
  --green-dark:#178257;
  --yellow:#f5b334;
  --ink:#1f1f1f;
  --muted:#555;
  --light:#f4f4f4;
  --white:#fff;
  --night:#3a3c3a;
}
*{margin:0;padding:0;box-sizing:border-box}
html,body{width:1200px;height:3660px;overflow:hidden}
body{position:relative;font-family:'Barlow',sans-serif;color:var(--ink);background:var(--light)}
.abs{position:absolute}
a{color:inherit;text-decoration:none}

/* header */
.top-rule{left:0;top:0;width:1200px;height:6px;background:linear-gradient(90deg,var(--teal) 0 51%,var(--yellow) 51% 100%)}
.site-header{left:0;top:6px;width:1200px;height:119px;background:var(--white)}
.brand{left:142px;top:32px;display:flex;align-items:center;gap:12px}
.brand-box{width:30px;height:30px;background:var(--teal)}
.brand-name{font-weight:700;font-size:27px;line-height:1;color:var(--ink);letter-spacing:.5px}
.brand-name small{display:block;font-size:19px;font-weight:700;letter-spacing:0;margin-top:4px}
.main-nav{top:57px;font-weight:600;font-size:16px}
.main-nav a.active{color:var(--yellow)}
.portal-btn{left:907px;top:47px;width:148px;height:41px;border:2px solid var(--yellow);border-radius:21px;color:var(--yellow);font-size:13px;font-weight:600;display:flex;align-items:center;justify-content:center;gap:5px}

/* hero */
.hero-photo{left:0;top:125px;width:1200px;height:600px;background:linear-gradient(90deg,#a2772d 0%,#8e6a35 25%,#6f6253 50%,#8b8476 75%,#b8ad95 100%)}
.hero-overlay{left:0;top:125px;width:222px;height:590px;background:rgba(245,179,52,.25)}
.hero-title{left:142px;top:214px;color:var(--white);font-weight:800;font-size:48px;line-height:62px;letter-spacing:.5px}
.hero-rule{left:142px;top:413px;width:479px;height:5px;background:linear-gradient(90deg,var(--teal) 0 66%,var(--white) 66%)}
.hero-sub{left:143px;top:448px;color:var(--white);font-size:20px;font-weight:500}
.quote-btn{left:143px;top:508px;width:160px;height:55px;border-radius:28px;background:var(--yellow);color:var(--white);font-weight:700;font-size:16px;display:flex;align-items:center;justify-content:center}
.hero-arrow{top:373px}

/* reasons */
.reasons-bg{left:0;top:714px;width:1200px;height:720px;background:radial-gradient(ellipse at 30% 40%,#ece4dc 0%,#f0ece7 40%,#f4f4f4 75%),#f4f4f4}
.section-title{width:1200px;left:0;text-align:center;font-weight:700;font-size:40px;letter-spacing:.3px}
.reason{width:280px}
.reason h3{font-weight:700;font-size:14px;letter-spacing:.3px;margin-bottom:6px}
.reason p{font-size:13.5px;line-height:20px;color:var(--muted)}
.reason.left{text-align:right}
.reason-num{font-weight:700;font-size:50px;color:var(--teal);line-height:1}
.reason-mark{left:562px;top:944px;width:120px;height:120px;border-radius:6px;background:var(--teal)}

/* about */
.about-text{left:597px;top:1440px;width:400px;color:var(--white)}
.about-text h2{font-weight:800;font-size:54px;letter-spacing:.5px;margin-bottom:18px}
.about-text p{font-size:12.5px;line-height:25px}
.read-btn{left:598px;top:1772px;width:163px;height:53px;border-radius:27px;background:var(--yellow);color:var(--white);font-weight:700;font-size:16px;display:flex;align-items:center;justify-content:center;gap:8px}
.about-frame{left:67px;top:1644px;width:250px;height:263px;border:4px solid var(--yellow)}
.about-photo{left:145px;top:1420px;width:389px;height:433px;background:linear-gradient(160deg,#3f4a3a 0%,#6d7d45 25%,#2d6f9a 55%,#c4c0b7 80%,#5b5147 100%)}

/* services */
.card{width:293px;height:417px;background:var(--white);border:1px solid #e2e2e2}
.card-photo{width:291px;height:217px}
.card-body{padding:22px 28px}
.card-body h3{font-weight:700;font-size:19px;line-height:24px;margin-bottom:12px}
.card-body p{font-size:11.5px;line-height:21px;color:var(--muted)}
.card-btn{position:absolute;left:28px;bottom:32px;width:110px;height:31px;transform:skewX(-20deg);display:flex;align-items:center;justify-content:center}
.card-btn span{transform:skewX(20deg);color:var(--white);font-weight:700;font-size:12px}
.card-btn.yellow{background:var(--yellow)}
.card-btn.teal{background:var(--teal)}

/* testimonial */
.quote-mark{left:258px;top:2818px;font-family:'Barlow',sans-serif;font-weight:800;font-size:150px;line-height:1;color:var(--yellow)}
.quote-text{left:378px;top:2846px;width:560px;color:var(--white);font-style:italic;font-size:19.5px;line-height:27px}
.quote-author{left:378px;top:3030px;color:var(--yellow);font-weight:700;font-style:italic;font-size:19px}
.recovery{left:90px;top:3010px;font-weight:800;font-style:italic;font-size:220px;color:rgba(255,255,255,.08);letter-spacing:4px;line-height:1}

/* footer */
.footer-brand{left:145px;top:3252px;display:flex;align-items:center;gap:10px}
.footer-brand .brand-box{width:22px;height:22px}
.footer-brand .brand-name{font-size:21px}
.footer-brand .brand-name small{font-size:15px}
.badge{top:3233px;height:58px}
.rule{left:145px;width:910px;height:1px;background:#dcdcdc}
.foot-col{top:3362px}
.foot-col h4{font-weight:500;font-size:15px;color:var(--muted);margin-bottom:16px}
.foot-col li{list-style:none;font-size:11.5px;line-height:21.7px;color:var(--muted)}
.contact-row{display:flex;gap:14px;align-items:flex-start;font-size:11.5px;line-height:17px;color:var(--muted);margin-bottom:22px}
.copyright{left:143px;top:3600px;font-size:12.5px;color:var(--muted)}
.social{top:3590px;display:flex;gap:8px;left:932px}
.social span{width:25px;height:25px;border-radius:50%;background:var(--green)}
.social span:last-child{background:var(--yellow)}
</style>
</head>
<body>

<!-- header -->
<div class="abs top-rule"></div>
<header class="abs site-header"></header>
<a class="abs brand" href="#"><span class="brand-box"></span><span class="brand-name">BRIGHTWAY<small>Workplace Partners</small></span></a>
<nav>
  <a class="abs main-nav" style="left:456px;color:var(--yellow)" href="#">Home</a>
  <a class="abs main-nav" style="left:523px" href="#">Services</a>
  <a class="abs main-nav" style="left:611px" href="#">About</a>
  <a class="abs main-nav" style="left:679px" href="#">Sap</a>
  <a class="abs main-nav" style="left:732px" href="#">Referrals</a>
  <a class="abs main-nav" style="left:824px" href="#">Contact</a>
</nav>
<a class="abs portal-btn" href="#">
  <svg width="10" height="11" viewBox="0 0 10 11"><circle cx="5" cy="3" r="2.6" fill="#f5b334"/><path d="M0 11c0-3.5 2.2-5 5-5s5 1.5 5 5z" fill="#f5b334"/></svg>CLIENT PORTAL</a>

<!-- hero -->
<div class="abs hero-photo" role="img" aria-label="Smiling worker in hard hat and safety glasses at an industrial site"></div>
<div class="abs hero-overlay"></div>
<svg class="abs" style="left:0;top:600px" width="1200" height="130"><polygon points="0,115 1200,25 1200,130 0,130" fill="#f4f4f4"/></svg>
<h1 class="abs hero-title">BRIGHTWAY<br>WORKPLACE<br>PARTNERS</h1>
<div class="abs hero-rule"></div>
<p class="abs hero-sub">We provide Mental Health Services for Employees</p>
<a class="abs quote-btn" href="#">GET A QUOTE</a>
<svg class="abs hero-arrow" style="left:82px" width="18" height="30"><polyline points="15,3 4,15 15,27" fill="none" stroke="#fff" stroke-width="3"/></svg>
<svg class="abs hero-arrow" style="left:1102px" width="18" height="30"><polyline points="3,3 14,15 3,27" fill="none" stroke="#fff" stroke-width="3"/></svg>

<!-- five reasons -->
<div class="abs reasons-bg" role="img" aria-label="Faded photo of a smiling family"></div>
<h2 class="abs section-title" style="top:766px">FIVE REASONS TO WORK WITH US</h2>
<div class="abs reason-mark"></div>

<div class="abs reason left" style="left:212px;top:934px"><h3>PELLENTESQUE FAUCIBUS</h3><p>Aliquam erat volutpat Quisque dignissim<br>congue leo Mauris vel lacus</p></div>
<span class="abs reason-num" style="left:503px;top:932px">1</span>
<div class="abs reason left" style="left:218px;top:1057px"><h3>PELLENTESQUE FAUCIBUS</h3><p>Aliquam erat volutpat Quisque dignissim<br>congue leo Mauris vel lacus</p></div>
<span class="abs reason-num" style="left:510px;top:1055px">2</span>

<span class="abs reason-num" style="left:711px;top:868px">3</span>
<div class="abs reason" style="left:749px;top:871px"><h3>PELLENTESQUE FAUCIBUS</h3><p>Aliquam erat volutpat Quisque dignissim<br>congue leo Mauris vel lacus</p></div>
<span class="abs reason-num" style="left:711px;top:983px">4</span>
<div class="abs reason" style="left:748px;top:986px"><h3>PELLENTESQUE FAUCIBUS</h3><p>Aliquam erat volutpat Quisque dignissim<br>congue leo Mauris vel lacus</p></div>
<span class="abs reason-num" style="left:707px;top:1122px">5</span>
<div class="abs reason" style="left:745px;top:1125px"><h3>PELLENTESQUE FAUCIBUS</h3><p>Aliquam erat volutpat Quisque dignissim<br>congue leo Mauris vel lacus</p></div>

<!-- about band -->
<svg class="abs" style="left:0;top:1225px" width="1200" height="820" role="img" aria-label="Green band over a faded aircraft cockpit photo">
  <defs><linearGradient id="band" x1="0" y1="0" x2="1" y2="1"><stop offset="0" stop-color="#1a8e62"/><stop offset=".5" stop-color="#22a070"/><stop offset="1" stop-color="#1e9a6c"/></linearGradient></defs>
  <polygon points="0,3 1200,195 1200,605 0,820" fill="url(#band)"/>
  <polygon points="1020,270 1200,205 1200,555 1020,520" fill="#ffffff"/>
</svg>
<div class="abs about-frame"></div>
<div class="abs about-photo" role="img" aria-label="Two pilots at the controls in an aircraft cockpit"></div>
<div class="abs about-text">
  <h2>ABOUT</h2>
  <p>Brightway Workplace Partners Inc. (“Brightway”) provides outstanding business-to-business services that support and promote health, wellness, and safety in the workplace. Brightway’s flagship programs are the Substance Abuse Professional (SAP) and Specialized Addiction Case Management services. Brightway is ready to provide organizations with access to a suite of best- practice solutions and options for your employees. These services empower organizations to effectively deal with substance use, to understand and fulfill various legislative and/or policy requirements, and to help keep their workers safe and healthy.</p>
</div>
<a class="abs read-btn" href="#">READ MORE
  <svg width="15" height="15" viewBox="0 0 15 15"><circle cx="7.5" cy="7.5" r="7.5" fill="#fff"/><polyline points="6,4 9.5,7.5 6,11" fill="none" stroke="#f5b334" stroke-width="2"/></svg></a>

<!-- services -->
<h2 class="abs section-title" style="top:2048px">OUR SERVICES</h2>
<article class="abs card" style="left:183px;top:2146px">
  <div class="card-photo" role="img" aria-label="Pilots in an aircraft cockpit" style="background:linear-gradient(160deg,#3d463a,#6c7c45 30%,#2f6e98 60%,#5b5147)"></div>
  <div class="card-body"><h3>Accomodation Screening</h3><p>Sed ut perspiciatis unde os iste natuserror sit voluptlom accusantium dolorlaoru dlu mtotam rem aperiamcusntm.</p></div>
  <a class="card-btn yellow" href="#"><span>READ MORE</span></a>
</article>
<article class="abs card" style="left:494px;top:2146px">
  <div class="card-photo" role="img" aria-label="Smiling call centre agent wearing a headset" style="background:linear-gradient(120deg,#c9c4bc,#e7e1d8 45%,#8a7a6b 70%,#d9d4cc)"></div>
  <div class="card-body"><h3>SAP Assessments</h3><p>Sed ut perspiciatis unde os iste natuserror sit voluptlom accusantium dolorlaoru dlu mtotam rem aperiamcusntm.</p></div>
  <a class="card-btn teal" href="#"><span>READ MORE</span></a>
</article>
<article class="abs card" style="left:802px;top:2146px">
  <div class="card-photo" role="img" aria-label="Construction workers in hard hats and safety vests at a site" style="background:linear-gradient(120deg,#6d8fc0,#c7d14a 35%,#d9c89a 65%,#b9c7d8)"></div>
  <div class="card-body"><h3>Specialized Addiction<br>Case Management</h3><p>Sed ut perspiciatis unde os iste natuserror sit voluptlom accusantium dolorlaoru.</p></div>
  <a class="card-btn teal" href="#"><span>READ MORE</span></a>
</article>

<!-- testimonial -->
<svg class="abs" style="left:0;top:2660px" width="1200" height="560" role="img" aria-label="Dark photo of an empty open road">
  <defs><linearGradient id="road" x1="0" y1="0" x2="0" y2="1"><stop offset="0" stop-color="#5a5d58"/><stop offset=".5" stop-color="#3f413e"/><stop offset="1" stop-color="#2e302d"/></linearGradient></defs>
  <polygon points="0,82 1200,0 1200,515 0,556" fill="url(#road)"/>
  <polygon points="900,535 1200,515 1200,495 1000,528" fill="#15a597"/>
</svg>
<div class="abs recovery">RECOVERY</div>
<div class="abs quote-mark">“</div>
<p class="abs quote-text">Sed ut perspiciatis unde omnis iste natus error sit voluptatem accusantium doloremque laudantium, totam rem aperiam, eaque ipsa quae ab illo inventore veritatis et quasi architecto beatae vit ae dicta sunt explicabo. Nemo enim ipsam voluptatem quia volupt as sit aspernatur aut odit aut fugit, sed quia consequuntur eos ratione voluptatem sequi nesciunt.</p>
<p class="abs quote-author">- Mara Ellison City Name</p>
<svg class="abs" style="left:1013px;top:3088px" width="46" height="32"><polyline points="14,3 3,16 14,29" fill="none" stroke="#ddd" stroke-width="2"/><polyline points="32,3 43,16 32,29" fill="none" stroke="#ddd" stroke-width="2"/></svg>

<!-- footer -->
<footer>
  <div class="abs" style="left:0;top:3218px;width:1200px;height:442px;background:var(--white)"></div>
  <a class="abs brand footer-brand" href="#"><span class="brand-box"></span><span class="brand-name">BRIGHTWAY<small>Workplace Partners</small></span></a>
  <div class="abs badge" style="left:755px;width:148px;border:2px solid #c9c9c9;background:#fafafa"></div>
  <div class="abs badge" style="left:907px;width:148px;background:#1c1c1c"></div>
  <div class="abs rule" style="top:3330px"></div>

  <div class="abs foot-col" style="left:145px">
    <h4>Contact</h4>
    <div class="contact-row"><svg width="18" height="22" viewBox="0 0 18 22"><path d="M9 1a7 7 0 0 1 7 7c0 5-7 13-7 13S2 13 2 8a7 7 0 0 1 7-7z" fill="none" stroke="#15a597" stroke-width="1.5"/><circle cx="9" cy="8" r="2.5" fill="none" stroke="#15a597" stroke-width="1.5"/></svg><span>48 Harbourview Lane, Suite 210<br>Riverton Ontario, K2P 4R7</span></div>
    <div class="contact-row"><svg width="20" height="20" viewBox="0 0 20 20"><path d="M4 2l3 0 2 5-2 1.5c1 2.5 3 4.5 5.5 5.5L14 12l5 2v3c0 1-1 2-2 2C9 18 2 11 1 4c0-1 1-2 3-2z" fill="none" stroke="#15a597" stroke-width="1.4"/></svg><span>555-014-2290<br>555-018-7731</span></div>
    <div class="contact-row"><svg width="24" height="18" viewBox="0 0 24 18"><rect x="1" y="1" width="22" height="16" fill="none" stroke="#15a597" stroke-width="1.4"/><polyline points="1,1 12,10 23,1" fill="none" stroke="#15a597" stroke-width="1.4"/></svg><span>Email:<br>hello@brightway-wp.example</span></div>
  </div>
  <div class="abs foot-col" style="left:429px"><h4>Projects</h4><ul><li>Lorem ipsum dolo</li><li>Consectetur adipiscing elit,</li><li>Fusce eget leo tincid</li><li>Donec consequat</li><li>Praesent elementum</li><li>Jmauris posueret</li><li>Aenean a ex eu lectu</li></ul></div>
  <div class="abs foot-col" style="left:661px"><h4>Company</h4><ul><li>Lorem ipsum dolo</li><li>Consectetur adipiscing elit,</li><li>Fusce eget leo tincid</li><li>Donec consequat</li><li>Praesent elementum</li><li>Jmauris posueret</li><li>Aenean a ex eu lectu</li></ul></div>
  <div class="abs foot-col" style="left:905px"><h4>Other Links</h4><ul><li>Lorem ipsum dolo</li><li>Consectetur adipiscing elit,</li><li>Fusce eget leo tincid</li><li>Donec consequat</li><li>Praesent elementum</li><li>Jmauris posueret</li><li>Aenean a ex eu lectu</li></ul></div>

  <div class="abs rule" style="top:3568px"></div>
  <p class="abs copyright">Copyright 2019 All Rights Reserved</p>
  <div class="abs social"><span></span><span></span><span></span><span></span></div>
</footer>
</body>
</html>
```